Flyer Photography modern, stylish classy

Edler and modern flyer makes people curious. 2 each representing my photographic activities generally. Appears to be: my logo, my address: Malte Vesperink Photographer in the house Dornhagen. . Kastanienweg 47 07391 Gera Tel (0365) 41 63 5 82 Email: Fotograf@MalteVesperink.eu Homepage: www.maltevesperink.eu Note from 01.06.2016 is from "picture atelier 9" "Malte Vesperink Photographer" with a new logo and a new location.

Project Deadline Extended Reason: Can not upload my full logo until 17.05.2016. Added Saturday, May 7, 2016

Target Market(s)

, To marry people aged 25 and over who are stylish and open-minded or simply want to have sophisticated images of themselves.

Font styles to use
Serif

Requirements
Must have
• Elegant and stylish look that makes one curious. It should radiate a valence and be modern. make to be photographed people like.
Nice to have
• The design of this general Flyers with the address data etc. (as described above) is can be applied to other topics-flyer like wedding, portrait - recognition.
Should not have
• loud colors

```html
<!DOCTYPE html>
<html lang="en">
<head>
<meta charset="utf-8">
<title>picture atelier 9 – Flyer</title>
<link href="https://fonts.googleapis.com/css2?family=Source+Sans+3:wght@400;700&display=swap" rel="stylesheet">
<style>
  :root {
    --header-bg: #ededed;
    --body-dark: #3b3b3d;
    --body-mid: #4a4a4c;
    --brand-red: #a8262c;
    --logo-grey: #8c8c8c;
    --text-light: #f2f2f2;
    --text-muted: #c9c9c9;
    --footer-bg: #ffffff;
    --ink: #2a2a2a;
    --frame: #ffffff;
  }
  * { box-sizing: border-box; margin: 0; padding: 0; }
  html, body { width: 940px; height: 1200px; overflow: hidden; background: #e4e4e4; }
  body { font-family: "Source Sans 3", Arial, sans-serif; }

  .flyer { position: relative; width: 940px; height: 1200px; overflow: hidden; }

  .flyer-header {
    position: absolute; left: 0; top: 0; width: 940px; height: 160px;
    background: var(--header-bg);
  }
  .brand { position: absolute; left: 40px; top: 34px; }
  .brand-name {
    font-weight: 700; font-size: 58px; line-height: 1; color: var(--logo-grey);
    letter-spacing: -1px;
  }
  .brand-owner {
    margin-top: 12px; font-size: 26px; color: var(--logo-grey);
    letter-spacing: 5px; text-align: center;
  }
  .contact-list { position: absolute; left: 628px; top: 40px; list-style: none; }
  .contact-list li {
    display: flex; align-items: center; gap: 14px; height: 32px;
    font-size: 18px; color: #555;
  }
  .contact-list svg { width: 18px; height: 18px; flex: none; }

  .flyer-body {
    position: absolute; left: 0; top: 160px; width: 940px; height: 963px;
    background: radial-gradient(ellipse at 45% 55%, var(--body-mid), var(--body-dark) 75%);
  }

  .photo {
    position: absolute; border: 6px solid var(--frame);
    box-shadow: 0 4px 10px rgba(0,0,0,.35);
  }
  .photo-vintage-car { left: 74px;  top: 42px;  width: 212px; height: 311px; background: linear-gradient(160deg,#d8d8d8,#4a4a4a 60%,#1e1e1e); }
  .photo-portrait-blue { left: 299px; top: 42px; width: 197px; height: 200px; background: radial-gradient(circle at 50% 40%,#b6c8d6,#3e6480 55%,#1b2f40); }
  .photo-wedding-cake { left: 514px; top: 42px; width: 326px; height: 306px; background: linear-gradient(135deg,#f2f2f2,#9a9a9a 50%,#2c2c2c); }
  .photo-couple-bouquet { left: 45px; top: 365px; width: 241px; height: 193px; background: linear-gradient(90deg,#8a8a8a,#2a2a2a 50%,#bdbdbd); }
  .photo-couple-garden { left: 299px; top: 256px; width: 197px; height: 302px; background: linear-gradient(180deg,#6b7a3e,#4d5a2c 50%,#8c6a4c); }
  .photo-red-legs { left: 514px; top: 365px; width: 355px; height: 193px; background: linear-gradient(100deg,#8fc0dc 35%,#b5313a 60%,#7fb4d4); }

  .cta-band {
    position: absolute; left: 0; top: 588px; width: 864px; height: 90px;
    background: var(--brand-red); box-shadow: 0 4px 10px rgba(0,0,0,.3);
  }
  .cta-text {
    position: absolute; left: 72px; top: 20px; font-size: 40px; color: #fff;
  }
  .photo-round {
    position: absolute; left: 619px; top: 533px; width: 184px; height: 184px;
    border-radius: 50%; border: 8px solid var(--frame);
    background: radial-gradient(circle at 50% 45%,#e2e2e2,#7a7a7a 60%,#3a3a3a);
    box-shadow: 0 4px 10px rgba(0,0,0,.35);
  }

  .motto {
    position: absolute; left: 37px; top: 728px; width: 863px;
    text-align: center; font-size: 24px; color: var(--text-light);
    padding-bottom: 8px; border-bottom: 1px solid #9a9a9a;
  }
  .owner-line {
    position: absolute; left: 0; top: 772px; width: 940px;
    text-align: center; font-size: 20px; color: var(--text-light);
  }
  .services {
    position: absolute; left: 0; top: 856px; width: 940px;
    text-align: center; font-size: 25px; line-height: 36px;
    color: var(--text-muted); letter-spacing: .5px;
  }

  .flyer-footer {
    position: absolute; left: 0; top: 1123px; width: 940px; height: 77px;
    background: var(--footer-bg);
  }
  .social-dot {
    position: absolute; left: 56px; top: 24px; width: 30px; height: 30px;
    border-radius: 50%; background: var(--ink);
  }
  .footer-url {
    position: absolute; left: 0; top: 16px; width: 940px; text-align: center;
    font-size: 36px; color: var(--ink); letter-spacing: .5px;
  }
</style>
</head>
<body>
<div class="flyer">
  <header class="flyer-header">
    <div class="brand">
      <div class="brand-name">picture atelier 9</div>
      <div class="brand-owner">Malte Vesperink</div>
    </div>
    <ul class="contact-list">
      <li>
        <svg viewBox="0 0 20 20" aria-hidden="true"><circle cx="10" cy="10" r="8.5" fill="none" stroke="#a8262c" stroke-width="1.8"/><path d="M7 5.5l1.8 2.4-1 1.2c.6 1.3 1.6 2.3 2.9 2.9l1.2-1 2.4 1.8-.9 1.6c-3.6-.4-6.9-3.7-7.3-7.3z" fill="#a8262c"/></svg>
        (0365) 41 63 5 82
      </li>
      <li>
        <svg viewBox="0 0 20 20" aria-hidden="true"><path d="M2 8l8-5 8 5v9H2z" fill="none" stroke="#a8262c" stroke-width="1.8" stroke-linejoin="round"/><path d="M2 8l8 5 8-5" fill="none" stroke="#a8262c" stroke-width="1.8"/></svg>
        Fotograf@MalteVesperink.eu
      </li>
      <li>
        <svg viewBox="0 0 20 20" aria-hidden="true"><circle cx="10" cy="10" r="8" fill="none" stroke="#a8262c" stroke-width="1.6"/><ellipse cx="10" cy="10" rx="3.5" ry="8" fill="none" stroke="#a8262c" stroke-width="1.4"/><path d="M2 10h16M3.5 6h13M3.5 14h13" stroke="#a8262c" stroke-width="1.2"/></svg>
        www.maltevesperink.eu
      </li>
    </ul>
  </header>

  <main class="flyer-body">
    <div class="photo photo-vintage-car" role="img" aria-label="Black and white photo of a woman posing on a vintage car"></div>
    <div class="photo photo-portrait-blue" role="img" aria-label="Portrait of a woman in a dark dress against a blue backdrop"></div>
    <div class="photo photo-wedding-cake" role="img" aria-label="Black and white photo of a bridal couple cutting their wedding cake"></div>
    <div class="photo photo-couple-bouquet" role="img" aria-label="Black and white photo of a bridal couple embracing with a bouquet"></div>
    <div class="photo photo-couple-garden" role="img" aria-label="Bridal couple standing among ivy by a wooden wall"></div>
    <div class="photo photo-red-legs" role="img" aria-label="Fashion shot of a woman in red trousers reclining against a light blue backdrop"></div>

    <div class="cta-band"><p class="cta-text">Book your session today!</p></div>
    <div class="photo-round" role="img" aria-label="Black and white portrait of a woman with a floral headpiece"></div>

    <p class="motto">„Schöne Bilder machen glücklich.“</p>
    <p class="owner-line">Malte Vesperink photographer in the house Dornhagen.</p>
    <p class="services">EXTRAVAGANT • HOCHZEIT • PORTRAIT • BEWERBUNG<br>EROTIK • FAMILIE • CATWALK</p>
  </main>

  <footer class="flyer-footer">
    <span class="social-dot" aria-hidden="true"></span>
    <p class="footer-url">www.maltevesperink.eu</p>
  </footer>
</div>
</body>
</html>
```